lunch promotion flyer

we recently started a new menu, would like to distribute the new menu and offer to the local office worker and residents.

Promotion Offer:
Pick any 2 delicious western Yum Cha for only $12
( Offer valid until 28/2/2015)
Updates

The flyer should contain the full menu and highlight the promotion, not just the promotion offer, it is totally wrong.

Target Market(s)

local office workers and local residents,

office workers are mainly working for the banks

Industry/Entity Type

Office

```html
<!DOCTYPE html>
<html lang="en">
<head>
<meta charset="utf-8">
<title>Quayside Kitchen – New Menu</title>
<link href="https://fonts.googleapis.com/css2?family=Arimo:wght@400;700&family=Dancing+Script:wght@700&display=swap" rel="stylesheet">
<style>
  :root {
    --ink: #111111;
    --blue: #1b3fd8;
    --navy: #1f2f9c;
    --red: #d7141a;
    --brown: #6b3a12;
    --gold: #d99a2b;
    --panel: #eef0f0;
    --leaf-soft: #dcebc4;
    --white: #ffffff;
  }
  * { box-sizing: border-box; margin: 0; padding: 0; }
  html, body { width: 864px; height: 1200px; overflow: hidden; background: var(--white); }
  body { font-family: "Arimo", Arial, sans-serif; color: var(--ink); }
  .flyer { position: relative; width: 864px; height: 1200px; overflow: hidden; }
  .abs { position: absolute; }

  .brand { left: 24px; top: 60px; display: flex; align-items: center; gap: 10px;
    font-size: 30px; font-weight: 700; color: var(--brown); }
  .brand-dot { width: 22px; height: 22px; border-radius: 50%; background: var(--gold); }
  .web { left: 37px; top: 146px; font-size: 16px; }

  .offer-badge { left: 604px; top: 18px; width: 196px; height: 196px; border-radius: 50%;
    border: 9px solid var(--navy); background: var(--white);
    display: flex; flex-direction: column; align-items: center; justify-content: center;
    text-align: center; font-size: 15px; line-height: 1.2; padding: 0 8px; white-space: nowrap; }
  .offer-badge .price { color: var(--red); font-size: 25px; line-height: 1.05; }

  .welcome { left: 69px; top: 186px; font-size: 37px; font-weight: 400; color: var(--blue); white-space: nowrap; }
  .intro { left: 69px; top: 240px; width: 660px; font-size: 15.3px; line-height: 1.3; }
  .team { left: 69px; top: 295px; font-size: 15.3px; }

  .info-panel { left: 69px; top: 322px; width: 471px; height: 245px; background: var(--panel); padding: 5px 10px 0 48px; }
  .script-head { font-family: "Dancing Script", cursive; font-size: 21px; color: var(--blue); text-decoration: underline; line-height: 26px; }
  .info-panel p { font-size: 16.5px; line-height: 20.6px; white-space: nowrap; }
  .info-panel .block + .block { margin-top: 30px; }

  .venue-photo { left: 540px; top: 312px; width: 324px; height: 288px;
    background: radial-gradient(ellipse at 40% 20%, #e8b89a 0%, #f4ddd0 35%, transparent 60%),
                linear-gradient(160deg, #fbf4f0 0%, #e9d6c9 50%, #c9a07a 80%, #8e5a36 100%); }

  .functions { left: 69px; top: 573px; color: var(--red); font-size: 16px; }
  .enquiry { left: 69px; top: 606px; font-size: 15.5px; line-height: 17.5px; }

  .happy-hour { left: 533px; top: 580px; width: 290px; height: 120px; }
  .happy-hour svg { position: absolute; inset: 0; }
  .happy-hour p { position: relative; text-align: center; color: var(--red); font-size: 14.5px; line-height: 1.15; padding-top: 16px; }

  .leaf-left { left: 0; top: 690px; width: 80px; height: 330px; background: linear-gradient(90deg, var(--leaf-soft), transparent); }
  .leaf-right { left: 690px; top: 820px; width: 174px; height: 380px; background: linear-gradient(200deg, var(--leaf-soft), transparent 80%); }

  .menu-title { left: 77px; top: 680px; font-family: "Dancing Script", cursive; font-size: 21px; color: var(--navy); text-decoration: underline; }
  .menu { left: 77px; top: 712px; width: 640px; }
  .menu h2 { font-size: 15.5px; font-weight: 400; color: var(--red); line-height: 17px; }
  .menu section + section { margin-top: 8px; }
  .menu-row { display: grid; grid-template-columns: 460px 103px 77px; font-size: 10.6px; line-height: 12.8px; white-space: nowrap; }
  .legend { left: 77px; top: 1101px; font-size: 10.6px; }
  .dine { left: 77px; top: 1121px; color: var(--red); font-size: 17.5px; }
  .feedback { left: 77px; top: 1143px; font-size: 16.5px; }
</style>
</head>
<body>
<main class="flyer">
  <div class="abs brand"><span class="brand-dot"></span>Quayside Kitchen</div>
  <div class="abs web">www.quaysidekitchen.example</div>

  <div class="abs offer-badge">
    <span>Pick any<br>2 delicious western<br>Yum Cha for</span>
    <span class="price">only $12</span>
    <span>( Offer valid until<br>28/2/2015)</span>
  </div>

  <h1 class="abs welcome">Welcome at Quayside Kitchen!</h1>
  <p class="abs intro">Share our Western Yum Cha amongst friends, family and colleagues, taste a summery salad,<br>let our steak sandwich surprise you or have a refreshing drink.</p>
  <p class="abs team">Our Quayside Kitchen team is happy to cater to any diet or allergy needs.</p>

  <div class="abs info-panel">
    <div class="block">
      <div class="script-head">We welcome you on:</div>
      <p>Monday – Wednesday 11.30 am – 4 pm<br>Thursday 11.30 am – 7 pm<br>Friday – Saturday 11.30 am – late</p>
    </div>
    <div class="block">
      <div class="script-head">Join us at:</div>
      <p>Waterfront side, Ground Floor, KBS building Shop 1,<br>412 Wharf Street, Portside<br>03 9000 4821<br>catering@quaysidekitchen.example</p>
    </div>
  </div>

  <div class="abs venue-photo" role="img" aria-label="Photo of the restaurant bar sign and steamer baskets of yum cha dumplings"></div>

  <p class="abs functions">Catering, Private &amp; Corporate functions available</p>
  <p class="abs enquiry">(7 am – 1 am)<br>Enquiries: 03 9000 4821<br>function@quaysidekitchen.example</p>

  <div class="abs happy-hour">
    <svg viewBox="0 0 290 120" width="290" height="120" aria-hidden="true">
      <ellipse cx="145" cy="60" rx="140" ry="55" fill="#ffffff" stroke="#6b3a12" stroke-width="6" stroke-dasharray="3 4"/>
      <ellipse cx="145" cy="60" rx="130" ry="47" fill="none" stroke="#d7141a" stroke-width="1.5" stroke-dasharray="2 3"/>
    </svg>
    <p>Happy Hour Drinks with<br>$1 and $2 tapas<br>See you every<br>Thursday and Friday<br>from 3pm to 7pm.</p>
  </div>

  <div class="abs leaf-left" role="img" aria-label="Green leafy branch decoration"></div>
  <div class="abs leaf-right" role="img" aria-label="Green leafy branch decoration"></div>

  <div class="abs menu-title">Kitchen healthy fresh new menu</div>
  <div class="abs menu">
    <section>
      <h2>Western Yum Cha</h2>
      <div class="menu-row"><span>Spanish Serrano ham &amp; cauliflower croquettes w saffron aioli</span><span></span><span>9</span></div>
      <div class="menu-row"><span>Spicy beef meatballs w rich tomato sugo &amp; yoghurt</span><span>GF</span><span>8</span></div>
      <div class="menu-row"><span>Garlic &amp; chili prawns- pan fried w crusty bread</span><span></span><span>13</span></div>
      <div class="menu-row"><span>Potato bravas – crispy fried potato w Spanish spicy tomato aioli</span><span>V/GF</span><span>6</span></div>
      <div class="menu-row"><span>Pesto arancini – Italian risotto ball w aioli</span><span></span><span>7</span></div>
      <div class="menu-row"><span>Beef shaslicks – marinated porterhouse beef, onion &amp; capsicum</span><span></span><span>13</span></div>
      <div class="menu-row"><span>Vegetarian rice paper rolls w hoisin dipping sauce</span><span>VG/GF</span><span>7</span></div>
      <div class="menu-row"><span>Crispy calamari – lightly fried w aioli &amp; lemon</span><span>GF</span><span>11</span></div>
      <div class="menu-row"><span>Bruschetta –warmed tomatoes , Spanish onion, basil &amp; fetta w balsamic glaze</span><span>V</span><span>9</span></div>
      <div class="menu-row"><span>Chicken drumettes , oven roasted w spicy plum sauce &amp; sesame seeds</span><span></span><span>8</span></div>
      <div class="menu-row"><span>Sweet corn &amp; coriander fritters , crunchy fried fritter w guacamole</span><span>V</span><span>9</span></div>
      <div class="menu-row"><span>sweet potato wafers , sumac salt seasoning w aioli</span><span>GF</span><span>7</span></div>
      <div class="menu-row"><span>Dips w warm Turkish pide</span><span></span><span>14</span></div>
    </section>
    <section>
      <h2>Salads</h2>
      <div class="menu-row"><span>Cucumber, honey dew w goats cheese dressing (+ chicken)</span><span>V</span><span>11 (14)</span></div>
      <div class="menu-row"><span>Rice noodles w crispy calamari &amp; vegetables</span><span>GF</span><span>13</span></div>
      <div class="menu-row"><span>Thai beef w Asian vegetables, lemongrass and crushed nuts</span><span></span><span>13</span></div>
      <div class="menu-row"><span>Gourmet tomato medley &amp; mixed beans w basil dressing</span><span>VG</span><span>10</span></div>
      <div class="menu-row"><span>Smoked salmon w tomato, Spanish onion &amp; fetta</span><span>GF</span><span>12</span></div>
    </section>
    <section>
      <h2>Bagels</h2>
      <div class="menu-row"><span>Smoked Salmon, dill cream cheese &amp; rocket</span><span></span><span>12</span></div>
      <div class="menu-row"><span>Chicken, cranberry &amp; brie</span><span></span><span>12</span></div>
      <div class="menu-row"><span>Prosciutto, roast capsicum, semi-dried tomato, rocket</span><span></span><span>12</span></div>
      <div class="menu-row"><span>Something substantial &amp; classic</span><span></span><span></span></div>
      <div class="menu-row"><span>Porterhouse steak sandwich with rocket, roast peppers, onions, cheese, dijonaise with chips</span><span></span><span>17.5</span></div>
      <div class="menu-row"><span>Classic Fish &amp; Chips, lightly fried fish with garden salad &amp; Chips</span><span></span><span>17.5</span></div>
    </section>
  </div>

  <p class="abs legend">GF = Gluten Free &nbsp;&nbsp; V = Vegetarian &nbsp;&nbsp;&nbsp;&nbsp; VG = Vegan</p>
  <p class="abs dine">Dine in or takeaway, please try Quayside</p>
  <p class="abs feedback">What do you think about our new menu? Your feedback will be much appreciated.</p>
</main>
</body>
</html>
```